Harbor Crest Physician Advising

I need a one-page advertisement that I can email to potential clients.

The target audience is hospital administrators.

I want it to include the logo, as attached. We specialize in Payer Denial Management. We are certified physician advisors with over 80 years combined clinical medicine experience. We have expertise in Utilization Management, Clinical Documentation Integrity, Peer to Peer Appeals and Letter Appeal Management. We win over 60% of our Peer to Peer Appeals with Medicare Advantage plans and over 50% of our first level letters.

We make sure hospitals get paid for the care they provide, I really want to emphasize that we are very effective at overturning insurance payment denials. We also provider other physician advising services. We keep our company small so that our rates are very affordable. Include that references are available.

We need to include: Contact us today, we can improve your revenue. Please 304-555-0183
or email (I will provide this later).

I want it to look professional but not bland, with maybe AI created images of a small group of physicians (mature, white coats, stethoscopes) looking at a spreadsheet on a laptop. a picture of a stack of money setting on a table, with a hand removing part of the money from the stack.

Companies like ours include Quorvix, T7, Pellingham, Car-Nova, and TelvanMD. Their websites may provide ideas.

Target Market(s)

Healthcare administrators who need to improve their hospital revenue

Industry/Entity Type

Healthcare consulting

Font styles to use
Sans Serif

Colors
0094D4
00A9DD
6FCCEA
C7EBF8
E9F6FB
00AB8E
00BBA5
67D7C9
C6EFE9
E9F9F6
FFC000
F8CF3A
FAE287
FDF2CF
FEFAEE
EE7325
F08F49
F5BC92
FAE3D3
FDF4ED
E54698
E96AAD
F1A4CE
F9D9EA
FCEFF6
6B429C
8869AF
B7A5CE
E3DAEB
F3F0F8

Requirements
Must have
• Must include that we are very successful here to appear in Peer to Peer appeals and Letter appeals
Nice to have
• Very easy to read, big bold fonts
Should not have
• I’m very afraid of having a lot of dark blues, combined with dark gold, because it may look like the colors of a health system in my area

```html
<!DOCTYPE html>
<html lang="en">
<head>
<meta charset="UTF-8">
<title>Harbor Crest Physician Advising</title>
<link href="https://fonts.googleapis.com/css2?family=Montserrat:wght@500;600;700;800&display=swap" rel="stylesheet">
<style>
  :root {
    --brand-blue: #0079d4;
    --accent-blue: #00a9dd;
    --charcoal: #444444;
    --ink: #555a5e;
    --white: #ffffff;
  }
  * { margin: 0; padding: 0; box-sizing: border-box; }
  html, body { width: 848px; height: 1200px; overflow: hidden; background: var(--white); }
  body { font-family: "Montserrat", Arial, sans-serif; }
  .flyer { position: relative; width: 848px; height: 1200px; overflow: hidden; background: var(--white); }

  .hero-photo {
    position: absolute; left: 0; top: 0; width: 848px; height: 550px;
    border-bottom-right-radius: 42px;
    background: linear-gradient(120deg, #f4f5f6 0%, #e4e7ea 45%, #d8e4ef 70%, #eceef0 100%);
  }

  .brand-mark { position: absolute; left: 18px; top: 22px; width: 216px; text-align: center; }
  .brand-mark .dot { display: block; width: 46px; height: 46px; border-radius: 50%; background: var(--brand-blue); margin: 0 auto 10px; }
  .brand-mark .name { font-weight: 700; font-size: 26px; color: var(--brand-blue); letter-spacing: -0.5px; line-height: 1; }
  .brand-mark .tag { font-weight: 600; font-size: 13.5px; color: var(--brand-blue); margin-top: 4px; letter-spacing: 0.2px; }

  .title-panel {
    position: absolute; left: 0; top: 331px; width: 516px; height: 282px;
    background: var(--brand-blue); border-radius: 0 42px 42px 0;
    color: var(--white); padding: 38px 0 0 58px;
  }
  .title-panel h1 { font-weight: 800; font-size: 80px; line-height: 72px; letter-spacing: -1px; }
  .title-panel .subtitle { font-weight: 700; font-size: 34px; margin-top: 14px; letter-spacing: 0.3px; }

  .service-pill {
    position: absolute; left: 0; width: 355px; height: 85px;
    background: var(--charcoal); border-radius: 0 43px 43px 0;
    display: flex; align-items: center; padding-left: 58px;
    color: var(--white); font-weight: 700; font-size: 23px; letter-spacing: 0.3px;
  }
  .service-pill .plus-badge {
    position: absolute; right: 17px; top: 15px; width: 55px; height: 55px;
    border-radius: 50%; background: var(--white);
    display: flex; align-items: center; justify-content: center;
  }
  .pill-one { top: 642px; }
  .pill-two { top: 748px; }

  .cross-decor { position: absolute; left: 396px; top: 782px; }

  .intro { position: absolute; left: 476px; top: 656px; width: 330px; }
  .intro h2 { font-weight: 700; font-size: 16px; color: var(--brand-blue); letter-spacing: 0.2px; margin-bottom: 4px; }
  .intro p { font-weight: 500; font-size: 14.4px; line-height: 23.8px; color: var(--ink); }

  .results-band { position: absolute; left: 0; top: 864px; width: 848px; height: 196px; background: var(--brand-blue); }
  .money-photo {
    position: absolute; left: 0; top: 8px; width: 269px; height: 180px;
    border-radius: 0 30px 30px 0;
    background: linear-gradient(135deg, #c9c4b6 0%, #dcdcd2 40%, #b9c2b8 75%, #a8ae9f 100%);
  }
  .result { position: absolute; top: 40px; width: 190px; color: var(--white); }
  .result h3 { font-weight: 700; font-size: 16px; letter-spacing: 0.4px; margin-bottom: 8px; }
  .result p { font-weight: 500; font-size: 14px; line-height: 16.6px; }
  .result-one { left: 325px; }
  .result-two { left: 582px; }
  .band-dots { position: absolute; left: 815px; top: 50px; }

  .contact-bar { position: absolute; left: 0; top: 1060px; width: 848px; height: 140px; background: var(--charcoal); color: var(--white); }
  .footer-dots { position: absolute; left: 55px; top: 18px; }
  .contact-item { position: absolute; top: 45px; }
  .contact-item .label { font-weight: 700; font-size: 12.5px; letter-spacing: 1.6px; }
  .contact-email { left: 202px; }
  .contact-email .value { font-weight: 600; font-size: 22.5px; margin-top: 8px; letter-spacing: 0.3px; }
  .contact-phone { left: 530px; }
  .contact-phone .value { font-weight: 800; font-size: 33px; margin-top: 2px; letter-spacing: 0.5px; }
</style>
</head>
<body>
<main class="flyer">
  <div class="hero-photo" role="img" aria-label="Photo of two physicians in white coats with stethoscopes reviewing data on a tablet"></div>

  <div class="brand-mark">
    <span class="dot"></span>
    <div class="name">HARBOR CREST</div>
    <div class="tag">PHYSICIAN ADVISING</div>
  </div>

  <section class="title-panel">
    <h1>HARBOR<br>CREST</h1>
    <div class="subtitle">PHYSICIAN ADVISING</div>
  </section>

  <div class="service-pill pill-one">P2P APPEALS
    <span class="plus-badge">
      <svg width="30" height="30" viewBox="0 0 30 30"><path d="M11 2h8v9h9v8h-9v9h-8v-9H2v-8h9z" fill="none" stroke="#00a9dd" stroke-width="2" stroke-linejoin="round"/></svg>
    </span>
  </div>
  <div class="service-pill pill-two">LETTER APPEALS
    <span class="plus-badge">
      <svg width="30" height="30" viewBox="0 0 30 30"><path d="M11 2h8v9h9v8h-9v9h-8v-9H2v-8h9z" fill="none" stroke="#00a9dd" stroke-width="2" stroke-linejoin="round"/></svg>
    </span>
  </div>

  <svg class="cross-decor" width="58" height="60" viewBox="0 0 58 60">
    <path d="M8 0h4v8h8v4h-8v8H8v-8H0V8h8z" fill="#00a9dd"/>
    <path d="M28 19h7v14h14v7H35v14h-7V40H14v-7h14z" fill="none" stroke="#00a9dd" stroke-width="2" stroke-linejoin="round"/>
  </svg>

  <section class="intro">
    <h2>PHYSICIAN ADVISING</h2>
    <p>Certified physician advisors with over 80 years combined clinical experience in Utilization Management, Clinical Documentation Integrity, Peer to Peer and Letter Appeals. References available.</p>
  </section>

  <section class="results-band">
    <div class="money-photo" role="img" aria-label="Photo of a hand taking banknotes from a stack of money on a table"></div>
    <div class="result result-one">
      <h3>PEER TO PEER</h3>
      <p>We win over 60% of our Peer to Peer Appeals with Medicare Advantage plans, so you get paid.</p>
    </div>
    <div class="result result-two">
      <h3>LETTER APPEALS</h3>
      <p>We win over 50% of our first level letters. Small team, affordable rates. Contact us today.</p>
    </div>
    <svg class="band-dots" width="30" height="100" viewBox="0 0 30 100" fill="#00a9dd">
      <circle cx="4" cy="2" r="2.4"/><circle cx="23" cy="2" r="2.4"/>
      <circle cx="4" cy="20.5" r="2.4"/><circle cx="23" cy="20.5" r="2.4"/>
      <circle cx="4" cy="39" r="2.4"/><circle cx="23" cy="39" r="2.4"/>
      <circle cx="4" cy="57.5" r="2.4"/><circle cx="23" cy="57.5" r="2.4"/>
      <circle cx="4" cy="76" r="2.4"/><circle cx="23" cy="76" r="2.4"/>
      <circle cx="4" cy="94.5" r="2.4"/><circle cx="23" cy="94.5" r="2.4"/>
    </svg>
  </section>

  <footer class="contact-bar">
    <svg class="footer-dots" width="100" height="102" viewBox="0 0 100 102" fill="#00a9dd">
      <g id="dot-row">
        <circle cx="4" cy="4" r="2.4"/><circle cx="22.3" cy="4" r="2.4"/><circle cx="40.6" cy="4" r="2.4"/><circle cx="58.9" cy="4" r="2.4"/><circle cx="77.2" cy="4" r="2.4"/><circle cx="95.5" cy="4" r="2.4"/>
      </g>
      <use href="#dot-row" y="18.5"/><use href="#dot-row" y="37"/><use href="#dot-row" y="55.5"/><use href="#dot-row" y="74"/><use href="#dot-row" y="92.5"/>
    </svg>
    <div class="contact-item contact-email">
      <div class="label">EMAIL</div>
      <div class="value">infocrest@hcmail.net</div>
    </div>
    <div class="contact-item contact-phone">
      <div class="label">CONTACT US</div>
      <div class="value">304-555-0183</div>
    </div>
  </footer>
</main>
</body>
</html>
```